Discreet simple classy for adult entertainment

I would like a matte black business card with gold writing for my business. Keeping it simple. Having my following:

Lana frost
Events. Entertainment. Promotions
0491726580

or alternatively could have what i had on my previous card below but i think i prefer the above as again - discretion.

Maybe a nice gold line thru the card or some other very simple design . Or not open to ideas/ can be doublesided if any good ideas with that.

included pics of my old bus card. not sure weather i want a photo on it or not. if i do it wont be the same pic. i kinda wanted a card that was discreet so if it was in someones wallet they wouldn't neccessarily realise it was from a stripper.

Target Market(s)

men

Industry/Entity Type

Business

Contact Information for Business Card

Lana frost
0491726580

Requirements
Nice to have
• i don't know i am really open to anything. im giving my cards to guys so something they can have in their wallet that is discreet preferably.

```html
<!DOCTYPE html>
<html lang="en">
<head>
<meta charset="utf-8">
<title>Lana Frost – Business Card</title>
<link href="https://fonts.googleapis.com/css2?family=Antonio:wght@100;200;300&display=swap" rel="stylesheet">
<style>
  :root {
    --backdrop: #2a2326;
    --card-black: #000000;
    --gold: #d9b24a;
    --gold-light: #f3d77a;
    --gold-deep: #a97f22;
    --photo-dark: #1d1a14;
    --photo-skin: #6b4a35;
    --photo-leaf: #1f2b17;
  }
  * { margin: 0; padding: 0; box-sizing: border-box; }
  html, body {
    width: 1200px; height: 1200px; overflow: hidden;
    background: var(--backdrop);
  }
  .canvas { position: relative; width: 1200px; height: 1200px; }
  .card {
    position: absolute; left: 294px; width: 659px; height: 373px;
    background: var(--card-black);
    overflow: hidden;
    box-shadow: 0 6px 14px rgba(0,0,0,0.45);
    font-family: "Antonio", "Arial Narrow", sans-serif;
    color: var(--gold);
  }
  .card--front { top: 186px; }
  .card--back { top: 620px; }

  .gold-text {
    background: linear-gradient(180deg, var(--gold-light) 0%, var(--gold) 50%, var(--gold-deep) 100%);
    -webkit-background-clip: text; background-clip: text;
    color: transparent;
  }

  .front-photo {
    position: absolute; left: 0; top: 0; width: 430px; height: 100%;
    background:
      linear-gradient(90deg, rgba(0,0,0,0) 55%, var(--card-black) 100%),
      radial-gradient(ellipse at 50% 45%, var(--photo-skin) 0%, var(--photo-dark) 55%, var(--photo-leaf) 100%);
  }
  .front-text {
    position: absolute; right: 30px; top: 0; width: 340px; height: 100%;
    text-align: right;
  }
  .name {
    position: absolute; right: 0; top: 26px;
    font-size: 56px; font-weight: 100; letter-spacing: 12px;
    white-space: nowrap; text-transform: uppercase; line-height: 1;
    margin-right: -12px;
  }
  .services {
    position: absolute; right: 0; top: 212px;
    list-style: none; white-space: nowrap;
  }
  .services li {
    font-size: 14px; font-weight: 200; letter-spacing: 4.2px;
    line-height: 22px; text-transform: uppercase;
  }
  .phone {
    position: absolute; right: 0; top: 308px;
    font-size: 42px; font-weight: 100; letter-spacing: 5px;
    line-height: 1; white-space: nowrap; margin-right: -5px;
  }

  .back-photo {
    position: absolute; left: 40px; top: 0; width: 226px; height: 100%;
    background:
      linear-gradient(90deg, var(--card-black) 0%, rgba(0,0,0,0) 25%, rgba(0,0,0,0) 70%, var(--card-black) 100%),
      linear-gradient(180deg, #5a4a36 0%, var(--photo-skin) 40%, #3a2a22 60%, var(--photo-skin) 100%);
  }
  .social {
    position: absolute; right: 50px; top: 294px;
    display: flex; align-items: center; gap: 10px;
  }
  .social-mark {
    width: 32px; height: 32px;
    background: linear-gradient(180deg, var(--gold-light), var(--gold-deep));
  }
  .social-handle { font-size: 18px; font-weight: 200; letter-spacing: 3px; }
</style>
</head>
<body>
<main class="canvas">
  <section class="card card--front">
    <div class="front-photo" role="img" aria-label="Portrait photo of the entertainer against garden foliage"></div>
    <div class="front-text">
      <h1 class="name gold-text">Lana Frost</h1>
      <ul class="services">
        <li class="gold-text">Events /</li>
        <li class="gold-text">Entertainment /</li>
        <li class="gold-text">Promotions /</li>
      </ul>
      <p class="phone gold-text">0491726580</p>
    </div>
  </section>

  <section class="card card--back">
    <div class="back-photo" role="img" aria-label="Photo of the entertainer in a black outfit, seen from behind"></div>
    <div class="social">
      <span class="social-mark"></span>
      <span class="social-handle gold-text">@LANAFROST</span>
    </div>
  </section>
</main>
</body>
</html>
```